I need a business card design for my new clinic (SPORTS MEDICINE OF KNEE). I am orthopedist, expert in sports surgery, especially knee surgery. I prefer, as colors, the colors of my logo (green, black and white). I already have my logo and should appear on my card. It's good to see my site to have ideas (www.drlucianovarela.com)
It needs contain:
my name: Dr. Luciano Varela
my registration: CRM 584-902
my specialty: Cirurgia do Joelho / Esporte
my address: Centro Executivo - Pinheiral Plaza
Av. Doutor Augusto Brandão Cunha, 2740 sala 0836
Jd. Ipanema - Ribeirão Preto - SP
my phone number: Tel (16) 8245-3908
my clinic phone: (16) 3670-4851
my e-mail: drlucianovarela@mailbox-exemplo.com
my site: www.drlucianovarela.com

Target Market(s)

futures patients

Industry/Entity Type

Clinic

Requirements
Nice to have
• letters not overfilled
straight lines, with few curves

```html
<!DOCTYPE html>
<html lang="pt-BR">
<head>
<meta charset="utf-8">
<title>Varela – Cartão de Visita</title>
<link rel="stylesheet" href="https://fonts.googleapis.com/css2?family=Crimson+Pro:wght@400;600;700&display=swap">
<style>
  :root {
    --green: #4fe651;
    --green-text: #3fd443;
    --ink: #1b1b1b;
    --paper: #ffffff;
    --edge: #cfcfcf;
    --page: #ffffff;
  }
  * { margin: 0; padding: 0; box-sizing: border-box; }
  html, body { width: 1200px; height: 960px; overflow: hidden; background: var(--page); }
  body { position: relative; font-family: "Crimson Pro", Georgia, serif; color: var(--ink); }

  .card {
    position: absolute;
    top: 48px;
    width: 554px;
    height: 880px;
    background: var(--paper);
    border: 2px solid var(--edge);
    box-shadow: 2px 3px 6px rgba(0,0,0,0.18);
    overflow: hidden;
  }
  .card--front { left: 30px; }
  .card--back { left: 612px; }

  .brand-name {
    font-weight: 600;
    font-size: 92px;
    line-height: 1;
    letter-spacing: 1px;
    color: var(--ink);
  }
  .brand-tagline {
    font-size: 22px;
    line-height: 28px;
    letter-spacing: 2px;
    color: var(--green-text);
  }

  /* Front */
  .card--front .brand-name {
    position: absolute; top: 52px; left: 0; width: 100%; text-align: center;
  }
  .card--front .brand-tagline {
    position: absolute; top: 142px; left: 0; width: 100%; text-align: center;
  }
  .front-specialty {
    position: absolute; top: 218px; left: 0; width: 100%; line-height: 48px;
    text-align: center; font-size: 38px; letter-spacing: -0.5px;
  }
  .brand-mark-area {
    position: absolute; left: 30px; top: 300px; width: 540px; height: 540px;
    border-radius: 36px;
    background: linear-gradient(135deg, var(--green) 0%, #3a8f3c 55%, var(--ink) 100%);
  }

  /* Back */
  .brand-square {
    position: absolute; top: 32px; left: 34px; width: 118px; height: 118px;
    background: var(--ink); border-radius: 10px;
  }
  .card--back .brand-name {
    position: absolute; top: 30px; left: 176px; font-size: 96px;
  }
  .card--back .brand-tagline {
    position: absolute; top: 120px; left: 190px; font-size: 22px;
  }

  .doctor-name {
    position: absolute; top: 200px; left: 0; width: 100%; line-height: 56px;
    text-align: center; font-size: 42px; font-weight: 400; letter-spacing: -0.5px;
  }
  .details { position: absolute; top: 282px; left: 34px; right: 10px; list-style: none; }
  .details li { height: 72px; line-height: 72px; font-size: 32px; letter-spacing: -0.6px; white-space: nowrap; }
  .details li.details__email { font-size: 25px; }
  .details .label { color: var(--green-text); }

  .address {
    position: absolute; top: 688px; left: 0; width: 100%;
    text-align: center; font-size: 20px; line-height: 36px; letter-spacing: -0.2px; font-style: normal;
  }
  .website {
    position: absolute; top: 812px; left: 0; width: 100%; line-height: 48px;
    text-align: center; font-size: 36px; font-weight: 700; color: var(--green-text);
  }
</style>
</head>
<body>
  <section class="card card--front">
    <div class="brand-name">VARELA</div>
    <div class="brand-tagline">Traumatologia Esportiva</div>
    <div class="front-specialty">Cirurgia do Joelho / Esporte</div>
    <div class="brand-mark-area" role="img" aria-label="Área da marca da clínica em verde e preto"></div>
  </section>

  <section class="card card--back">
    <div class="brand-square"></div>
    <div class="brand-name">VARELA</div>
    <div class="brand-tagline">Traumatologia Esportiva</div>
    <h1 class="doctor-name">Dr. Luciano Varela</h1>
    <ul class="details">
      <li><span class="label">registration:</span> CRM 584-902</li>
      <li><span class="label">specialty:</span> Cirurgia do Joelho / Esporte</li>
      <li><span class="label">tel:</span> (16) 8245-3908</li>
      <li><span class="label">clinic tel:</span> (16) 3670-4851</li>
      <li class="details__email"><span class="label">e-mail:</span> drlucianovarela@mailbox-exemplo.com</li>
    </ul>
    <address class="address">
      Centro Executivo - Pinheiral Plaza<br>
      Av. Doutor Augusto Brandão Cunha, 2740 sala 0836<br>
      Jd. Ipanema - Ribeirão Preto - SP
    </address>
    <div class="website">www.drlucianovarela.com</div>
  </section>
</body>
</html>
```